IT Company that provides secure IT solutions and services to our customers

We need business cards and a logo for a new IT Solutions company just created based in Kuala Lumpur, Malaysia. But will also be serving other countries in the region. We provide secure data, voice solutions on mobile platforms. Our first offering is encrypted voice and data solutions for IOS, Android, Windows and BlackBerry devices.

Target Market(s)

large organizations Govt, Police, Defence, Anti-corruption, Legal, highly regulated industries such as Health-care, Financial, Banking, Insurance,

Industry/Entity Type

Information Technology

Contact Information for Business Card

VornaxIT (Logo - colour is ORBEL blue)Dariush Pelo Managing Director Vornax IT Sdn. Bhd.5th Floor, Block F, Wisma LBD,No.14 Jalan Seri Mewah,50470, Kuala LumpurMalaysia

Font styles to use
Sans Serif

Colors
3176b5
ec1f27
fbed22

Requirements
Must have
• VornaxIT all in Blue like ORBEL blue. A logo design perhaps a play of VI, K with a dangling T (colour can be any)
Nice to have
• I want a clean crisp card, not too busy, easy to read.

```html
<!DOCTYPE html>
<html lang="en">
<head>
<meta charset="utf-8">
<title>VornaxIT Business Card</title>
<link href="https://fonts.googleapis.com/css2?family=Montserrat:wght@700&family=Questrial&display=swap" rel="stylesheet">
<style>
  :root {
    --stage: #1a1a1a;
    --card: #2b2b2b;
    --white: #ffffff;
    --text: #e6e6e6;
    --brand-blue: #3f6fc1;
    --icon-blue: #3f68b8;
    --rule: #8a8a8a;
  }
  * { margin: 0; padding: 0; box-sizing: border-box; }
  html, body { width: 1200px; height: 1021px; overflow: hidden; background: var(--stage); }
  body { position: relative; font-family: "Questrial", sans-serif; }

  .card {
    position: absolute;
    width: 560px;
    height: 320px;
    background: var(--card);
    border-radius: 2px;
  }
  .card-front { left: 80px; top: 100px; display: flex; align-items: center; justify-content: center; }
  .card-back { left: 560px; top: 580px; }

  .wordmark {
    font-family: "Montserrat", sans-serif;
    font-weight: 700;
    letter-spacing: 0.5px;
  }
  .card-front .wordmark { color: var(--white); font-size: 40px; }

  .back-logo {
    position: absolute;
    left: 40px;
    top: 165px;
    display: flex;
    align-items: center;
    gap: 12px;
  }
  .back-logo .mark-dot { width: 16px; height: 16px; border-radius: 50%; background: var(--brand-blue); }
  .back-logo .wordmark { color: var(--brand-blue); font-size: 38px; }

  .divider {
    position: absolute;
    left: 262px;
    top: 60px;
    width: 1px;
    height: 210px;
    background: var(--rule);
  }

  .details { position: absolute; left: 280px; top: 54px; color: var(--text); }
  .person-name { font-family: "Montserrat", sans-serif; font-weight: 700; font-size: 15px; color: var(--white); }
  .person-title { font-size: 11px; color: var(--white); margin-bottom: 12px; }

  .contact-list { list-style: none; font-size: 12.5px; line-height: 20px; margin-bottom: 14px; }
  .contact-list li { display: flex; align-items: center; gap: 9px; }
  .contact-list svg { width: 12px; height: 12px; fill: var(--icon-blue); flex-shrink: 0; }

  .address { font-size: 12.5px; line-height: 20px; }
</style>
</head>
<body>

  <section class="card card-front" aria-label="Card front">
    <div class="wordmark">VornaxIT</div>
  </section>

  <section class="card card-back" aria-label="Card back">
    <div class="back-logo">
      <span class="mark-dot"></span>
      <span class="wordmark">VornaxIT</span>
    </div>

    <div class="divider"></div>

    <div class="details">
      <div class="person-name">Dariush Pelo</div>
      <div class="person-title">Managing Director</div>

      <ul class="contact-list">
        <li>
          <svg viewBox="0 0 12 12" aria-hidden="true"><path d="M1 3c0-1 1-2 2.5-2h5C10 1 11 2 11 3v1H8V3H4v1H1zM3 5h6l2 5H1z"/></svg>
          603 XXX XXXX
        </li>
        <li>
          <svg viewBox="0 0 12 12" aria-hidden="true"><path d="M3 1h6v3H3zM1 5h10v5H9V8H3v2H1zM3.5 8.5h5V11h-5z"/></svg>
          603 XXX XXXX
        </li>
        <li>
          <svg viewBox="0 0 12 12" aria-hidden="true"><path d="M1 3h10v6H1zM1.5 3.5L6 7l4.5-3.5" stroke="#2b2b2b" stroke-width="0.8"/></svg>
          info@vornaxIT.com
        </li>
        <li>
          <svg viewBox="0 0 12 12" aria-hidden="true"><circle cx="6" cy="6" r="5"/><path d="M1 6h10M6 1c2 2 2 8 0 10M6 1c-2 2-2 8 0 10" stroke="#2b2b2b" stroke-width="0.7" fill="none"/></svg>
          www.vornaxIT.com
        </li>
      </ul>

      <div class="address">
        Vornax IT Sdn. Bhd. 5th Floor, Block F<br>
        Wisma LBD, No.14 Jalan Seri Mewah<br>
        50470, Kuala Lumpur Malaysia
      </div>
    </div>
  </section>

</body>
</html>
```